Album/CD cover art for album named Velvet Harbors, by the band Marble Sundown

I would like an album cover. The album will have a wreath of flowers similar to the first file download. In two of the flowers (white large) will the drawn faces of the two pictures attached. The bird flying out of the wreath will be a Falcon.

```html
<!DOCTYPE html>
<html lang="en">
<head>
<meta charset="utf-8">
<title>Velvet Harbors — Marble Sundown</title>
<link rel="stylesheet" href="https://fonts.googleapis.com/css2?family=Londrina+Solid:wght@400;900&display=swap">
<style>
  :root {
    --page-bg: #ffffff;
    --cover-deep: #14040a;
    --cover-mid: #300c16;
    --text-blush: #f3cbc5;
    --text-white: #ffffff;
    --wreath-green: #a9d0a0;
    --wreath-peach: #f4cfae;
    --wreath-blue: #9db8ea;
    --wreath-pink: #eab3c3;
    --portrait-cream: #f3eee9;
    --portrait-peach: #f5caa8;
    --falcon-brown: #8c6c60;
    --falcon-dark: #4d3129;
    --sparkle: #b9c4e0;
  }
  * { margin: 0; padding: 0; box-sizing: border-box; }
  html, body { width: 846px; height: 1200px; overflow: hidden; }
  body {
    background: var(--page-bg);
    font-family: "Londrina Solid", "Arial Narrow", sans-serif;
    position: relative;
  }
  .album-cover {
    position: absolute;
    left: 33px; top: 210px;
    width: 780px; height: 780px;
    background: radial-gradient(circle at 48% 56%, var(--cover-mid) 0%, var(--cover-deep) 80%);
    overflow: hidden;
  }
  .cover-art { position: absolute; inset: 0; }
  .credits {
    position: absolute; left: 31px; top: 22px;
    text-transform: uppercase; letter-spacing: 1px;
    font-size: 27px; line-height: 35px; font-weight: 400;
  }
  .credits .band, .credits .artist { color: var(--text-blush); }
  .credits .album-title { color: var(--text-white); font-size: 27px; font-weight: 400; }
  .catalog {
    position: absolute; left: 31px; top: 684px;
    color: var(--text-white); text-transform: uppercase;
  }
  .catalog-number { font-size: 36px; font-weight: 900; line-height: 38px; letter-spacing: 1px; }
  .catalog-series { font-size: 14px; letter-spacing: 2px; margin-top: 6px; color: var(--text-blush); }
  .label-mark {
    position: absolute; left: 651px; top: 652px;
    width: 98px; height: 98px;
    display: flex; align-items: center; justify-content: center;
  }
  .label-mark .ring {
    position: absolute; inset: 0;
    border: 2px solid var(--text-white); border-radius: 50%;
  }
  .label-mark .name {
    color: var(--text-white); font-size: 19px; letter-spacing: 1px;
    text-transform: uppercase;
  }
</style>
</head>
<body>
  <main class="album-cover">
    <svg class="cover-art" width="780" height="780" viewBox="0 0 780 780">
      <defs>
        <filter id="soften" x="-30%" y="-30%" width="160%" height="160%">
          <feGaussianBlur stdDeviation="6"/>
        </filter>
        <filter id="haze" x="-30%" y="-30%" width="160%" height="160%">
          <feGaussianBlur stdDeviation="14"/>
        </filter>
        <linearGradient id="sparkleTone" x1="0" y1="0" x2="1" y2="0">
          <stop offset="0" stop-color="var(--sparkle)" stop-opacity="0"/>
          <stop offset="0.5" stop-color="var(--sparkle)" stop-opacity="0.28"/>
          <stop offset="1" stop-color="var(--sparkle)" stop-opacity="0"/>
        </linearGradient>
        <linearGradient id="wreathTone" x1="0" y1="0" x2="1" y2="1">
          <stop offset="0" stop-color="var(--wreath-pink)"/>
          <stop offset="0.3" stop-color="var(--wreath-green)"/>
          <stop offset="0.55" stop-color="var(--wreath-peach)"/>
          <stop offset="0.8" stop-color="var(--wreath-blue)"/>
          <stop offset="1" stop-color="var(--wreath-green)"/>
        </linearGradient>
        <radialGradient id="falconTone" cx="0.45" cy="0.45" r="0.55">
          <stop offset="0" stop-color="var(--falcon-brown)"/>
          <stop offset="0.7" stop-color="var(--falcon-dark)" stop-opacity="0.9"/>
          <stop offset="1" stop-color="var(--falcon-dark)" stop-opacity="0"/>
        </radialGradient>
        <radialGradient id="creamBloom" cx="0.5" cy="0.5" r="0.5">
          <stop offset="0" stop-color="var(--portrait-cream)"/>
          <stop offset="0.8" stop-color="var(--portrait-cream)" stop-opacity="0.9"/>
          <stop offset="1" stop-color="var(--portrait-cream)" stop-opacity="0"/>
        </radialGradient>
        <radialGradient id="peachBloom" cx="0.5" cy="0.5" r="0.5">
          <stop offset="0" stop-color="var(--portrait-peach)"/>
          <stop offset="0.8" stop-color="var(--portrait-peach)" stop-opacity="0.9"/>
          <stop offset="1" stop-color="var(--portrait-peach)" stop-opacity="0"/>
        </radialGradient>
      </defs>

      <g class="sparkle-bands" role="img" aria-label="Soft bands of drifting sparkles across the night background" filter="url(#haze)">
        <polygon points="0,355 0,440 540,590 560,520" fill="url(#sparkleTone)"/>
        <polygon points="600,380 780,320 780,420 640,470" fill="url(#sparkleTone)"/>
        <polygon points="680,180 780,60 780,200 720,250" fill="url(#sparkleTone)"/>
      </g>

      <circle class="flower-wreath" role="img" aria-label="Watercolour wreath of peonies, roses and leaves"
              cx="378" cy="437" r="268" fill="none" stroke="url(#wreathTone)" stroke-width="66"
              opacity="0.9" filter="url(#soften)"/>

      <ellipse class="falcon-illustration" role="img" aria-label="Illustrated falcon flying out of the wreath"
               cx="652" cy="212" rx="100" ry="145" transform="rotate(-20 652 212)" fill="url(#falconTone)"/>

      <ellipse class="portrait-upper" role="img" aria-label="Portrait of a band member set in a large white flower"
               cx="212" cy="251" rx="122" ry="118" fill="url(#creamBloom)"/>
      <ellipse class="portrait-lower" role="img" aria-label="Portrait of a band member set in a large peach flower"
               cx="498" cy="590" rx="112" ry="126" fill="url(#peachBloom)"/>
    </svg>

    <header class="credits">
      <p class="band">Marble Sundown</p>
      <p class="artist">Ada Quillon</p>
      <h1 class="album-title">Velvet Harbors</h1>
    </header>

    <footer class="catalog">
      <p class="catalog-number">0013</p>
      <p class="catalog-series">LNR x Sundown</p>
    </footer>

    <div class="label-mark">
      <span class="ring"></span>
      <span class="name">Sundown</span>
    </div>
  </main>
</body>
</html>
```